Need a business card for our overland brand!

We had the logo made and we need a great design for our business card. Use the logo provide or tweak it however you see fit.

Contact Information for Business Card

Name, Title, Telephone, email, website

```html
<!DOCTYPE html>
<html lang="en">
<head>
<meta charset="utf-8">
<title>Northline Trails — Business Card</title>
<link href="https://fonts.googleapis.com/css2?family=Montserrat:wght@300;400;700;800&display=swap" rel="stylesheet">
<style>
  :root {
    --navy: #253850;
    --teal: #1c9dbf;
    --white: #ffffff;
    --ink: #2a2f36;
    --stage: #1b1b1d;
  }
  * { margin: 0; padding: 0; box-sizing: border-box; }
  html, body { width: 1200px; height: 934px; overflow: hidden; background: var(--stage); }
  body { font-family: "Montserrat", Arial, sans-serif; position: relative; }

  .card {
    position: absolute;
    left: 220px;
    width: 760px;
    height: 434px;
    overflow: hidden;
    border-radius: 2px;
  }
  .card--front { top: 24px; background: var(--teal); }
  .card--back { top: 476px; background: var(--white); }

  .front-shape { position: absolute; inset: 0; width: 100%; height: 100%; }

  .brand {
    font-weight: 800;
    text-transform: uppercase;
    line-height: 0.92;
    letter-spacing: 1px;
  }
  .brand--front {
    position: absolute;
    left: 0; right: 0; top: 142px;
    text-align: center;
    color: var(--white);
    font-size: 74px;
  }
  .brand--back {
    position: absolute;
    right: 60px; top: 52px;
    color: var(--navy);
    font-size: 42px;
    text-align: left;
  }

  .rule {
    position: absolute;
    height: 1.5px;
    background: var(--ink);
  }
  .rule--top { left: 330px; right: 50px; top: 178px; }
  .rule--contact { left: 60px; width: 270px; top: 298px; }

  .person { position: absolute; left: 60px; top: 228px; color: var(--navy); }
  .person__name { font-weight: 800; font-size: 26px; letter-spacing: 0.5px; text-transform: uppercase; }
  .person__title { font-weight: 400; font-size: 17px; letter-spacing: 1px; text-transform: uppercase; margin-top: 4px; }

  .contact { position: absolute; left: 60px; top: 316px; list-style: none; }
  .contact__item {
    display: flex; align-items: center; gap: 14px;
    font-size: 15px; font-weight: 400; color: var(--ink);
    height: 30px;
  }
  .contact__icon { width: 20px; height: 20px; flex: none; }

  .address {
    position: absolute; right: 50px; top: 330px;
    text-align: right;
    font-size: 15px; line-height: 1.45; color: var(--ink);
  }
</style>
</head>
<body>

  <section class="card card--front" aria-label="Card front">
    <svg class="front-shape" viewBox="0 0 760 434" preserveAspectRatio="none" aria-hidden="true">
      <path d="M120 0 H640 C700 120 705 320 640 434 H120 C55 320 60 120 120 0 Z" fill="#253850"/>
      <path d="M118 30 C88 160 90 300 122 420" fill="none" stroke="#1c9dbf" stroke-width="3"/>
      <path d="M642 30 C672 160 670 300 638 420" fill="none" stroke="#1c9dbf" stroke-width="3"/>
    </svg>
    <div class="brand brand--front">Northline<br>Trails</div>
  </section>

  <section class="card card--back" aria-label="Card back">
    <div class="brand brand--back">Northline<br>Trails</div>
    <div class="rule rule--top"></div>

    <div class="person">
      <div class="person__name">Daniel Harper</div>
      <div class="person__title">Managing Director</div>
    </div>
    <div class="rule rule--contact"></div>

    <ul class="contact">
      <li class="contact__item">
        <svg class="contact__icon" viewBox="0 0 24 24" aria-hidden="true"><path fill="#1c9dbf" d="M6.6 10.8a15.1 15.1 0 0 0 6.6 6.6l2.2-2.2a1 1 0 0 1 1-.25 11.4 11.4 0 0 0 3.6.57 1 1 0 0 1 1 1V20a1 1 0 0 1-1 1A17 17 0 0 1 3 4a1 1 0 0 1 1-1h3.5a1 1 0 0 1 1 1c0 1.25.2 2.45.57 3.57a1 1 0 0 1-.25 1z"/></svg>
        044-555 210 347
      </li>
      <li class="contact__item">
        <svg class="contact__icon" viewBox="0 0 24 24" aria-hidden="true"><rect x="2" y="5" width="20" height="14" rx="1.5" fill="#1c9dbf"/><path d="M3 6.5l9 6.5 9-6.5" fill="none" stroke="#fff" stroke-width="1.6"/></svg>
        info@northlinetrails.com
      </li>
      <li class="contact__item">
        <svg class="contact__icon" viewBox="0 0 24 24" aria-hidden="true"><circle cx="12" cy="12" r="10" fill="#1c9dbf"/><path d="M2 12h20M12 2c3 3 3 17 0 20M12 2c-3 3-3 17 0 20" fill="none" stroke="#fff" stroke-width="1.4"/></svg>
        www.northlinetrails.com
      </li>
    </ul>

    <address class="address" style="font-style:normal">
      421, Address line goes here<br>
      45452, Country name
    </address>
  </section>

</body>
</html>
```